Coach/consultant in conflict and challenge needs an enticing flyer

I need a double sided DL flyer design that will describe my work in helping people meet conflict and emotional challenge so they can learn and grow from these difficulties. I want to give a flavour of my style through fresh colours, repeated images used differently (the spiral), and a sense of positivity around conflict and difficulty. I want to attract people who are keen to do things differently and want to engage with creative processes rather than getting stuck in familiar patterns. My work is creative and often includes use of story, images and fables, so I want to convey that as well. I also place the work in a spiritual context, but grounded in practicality so I don't want it to seem New Age or flakey. I want something that seems innovative, professional and intriguing. I've included a sample of something I mocked up in word and also a copy of a flyer for Marla Quennet's Ember Gathering that inspired me to get a DL flyer. I want the design to communicate trust and transformation and engaging with fresh ways of doing things by moving past old habits

Target Market(s)

Mid 30s plus women and men who want to change their approach to conflict and emotional difficulties and are willing to take the creative and challenging journey to do that

Industry/Entity Type

Learn

Colors
acd136
00a990

Requirements
Must have
• a shift in the use of the spiral image,
• use of image of me (Norah)
• bright fresh colours olours that represent growth and transformation--I've suggested lime green as it suggests a sense of growth
• easy to read text
Nice to have
• Interesting non-traditional fonts perhaps text in a contemporary sans serif and another brush script font (like the Ember Gathering example)
• bleed to the edge and run off the page images or text
Should not have
• anything that represents too much tradition or stuckness

```html
<!DOCTYPE html>
<html lang="en">
<head>
<meta charset="utf-8">
<title>Norah Pellow – DL Flyer</title>
<link rel="stylesheet" href="https://fonts.googleapis.com/css2?family=Kaushan+Script&family=Montserrat:wght@400;500&family=Parisienne&display=swap">
<style>
  :root {
    --page: #e2fbb4;
    --teal: #02a98f;
    --teal-deep: #04996f;
    --lime: #acd136;
    --white: #ffffff;
    --brown: #8a5a3b;
    --brown-light: #b78b5c;
    --rust: #a44a2c;
    --orange: #d9602e;
  }
  * { margin: 0; padding: 0; box-sizing: border-box; }
  html, body { width: 1200px; height: 1200px; overflow: hidden; }
  body { background: var(--page); position: relative; font-family: "Montserrat", sans-serif; }

  .flyer-side {
    position: absolute; left: 54px; width: 1096px; height: 517px;
    background: var(--teal); overflow: hidden;
    box-shadow: 0 6px 14px rgba(60, 80, 40, 0.35);
  }
  .flyer-side--front { top: 58px; }
  .flyer-side--back { top: 618px; }

  .script-name {
    position: absolute; font-family: "Kaushan Script", cursive; font-weight: 400;
    line-height: 1; white-space: nowrap;
  }

  /* front */
  .spiral-art {
    position: absolute; left: 590px; top: 24px; width: 496px; height: 470px;
    background: radial-gradient(ellipse 50% 50% at 55% 50%, rgba(138,90,59,0.85) 0%, rgba(160,110,70,0.65) 45%, rgba(2,169,143,0) 100%);
  }
  .front-name { left: 40px; top: 80px; font-size: 118px; color: var(--lime); }
  .values {
    position: absolute; left: 56px; top: 240px; font-size: 25.5px; font-weight: 500;
    color: var(--white); letter-spacing: 0.5px; white-space: nowrap;
  }
  .values .dot { color: var(--rust); margin: 0 6px; }
  .intro {
    position: absolute; left: 49px; top: 285px; width: 530px;
    font-size: 16.5px; line-height: 22.5px; color: var(--lime);
  }

  /* back */
  .back-swirl {
    position: absolute; inset: 0;
    background:
      radial-gradient(ellipse 340px 300px at 330px 260px, rgba(3,150,110,0.35) 0%, rgba(2,169,143,0) 100%),
      radial-gradient(ellipse 260px 220px at 720px 110px, rgba(3,150,110,0.4) 0%, rgba(2,169,143,0) 80%);
  }
  .portrait {
    position: absolute; left: 784px; top: 0; width: 312px; height: 517px;
    background: linear-gradient(180deg, #6f6f6f 0%, #8a8079 20%, #c79a82 32%, var(--orange) 50%, #c95426 100%);
  }
  .about {
    position: absolute; left: 42px; top: 64px; width: 620px;
    font-size: 16.5px; line-height: 22px; color: var(--lime);
  }
  .services { position: absolute; left: 52px; top: 238px; list-style: none; }
  .services li {
    font-family: "Parisienne", cursive; font-size: 25px; color: var(--white);
    height: 36px; display: flex; align-items: center; gap: 8px;
  }
  .services svg { width: 14px; height: 14px; }
  .back-name { left: 352px; top: 226px; font-size: 112px; color: var(--white); }
  .credentials {
    position: absolute; left: 360px; top: 356px; font-size: 15px; line-height: 22px; color: var(--lime);
  }
  .contact { position: absolute; font-size: 18px; line-height: 24px; }
  .contact--phone { left: 42px; top: 428px; color: var(--lime); }
  .contact--web { left: 358px; top: 428px; color: var(--lime); }
  .contact--web .site { color: var(--white); }
</style>
</head>
<body>
  <section class="flyer-side flyer-side--front">
    <div class="spiral-art" role="img" aria-label="Brown watercolour brush-stroke spiral"></div>
    <h1 class="script-name front-name">Norah Pellow</h1>
    <p class="values">COURAGE<span class="dot">•</span>LISTENING<span class="dot">•</span>CREATIVITY</p>
    <p class="intro">Challenge, change and conflict are a natural part of life. When we greet them with courage, and listen to what they tell us, we grow in wisdom, resilience and creativity.<br>Norah Pellow is a coach, educator and mediator. She works with people who want to harvest the fruits of challenge and conflict so they live life differently.</p>
  </section>

  <section class="flyer-side flyer-side--back">
    <div class="back-swirl"></div>
    <div class="portrait" role="img" aria-label="Portrait photograph of Norah in an orange knitted top"></div>
    <p class="about">Consult with Norah to address challenges in your life, relationship, group or organisation. Through listening, conversation and creative processes, you will discover what your challenge is asking of you. Norah Pellow is a skilled facilitator who works to shift people’s responses from reactivity to creativity. With many years’ experience in coaching and mentorship, mediation and narrative processes, Norah supports you to uncover unique responses to difficult situations.</p>
    <ul class="services">
      <li><svg viewBox="0 0 14 14"><circle cx="7" cy="7" r="5" fill="none" stroke="var(--rust)" stroke-width="2"/></svg>consultations</li>
      <li><svg viewBox="0 0 14 14"><circle cx="7" cy="7" r="5" fill="none" stroke="var(--rust)" stroke-width="2"/></svg>workshops</li>
      <li><svg viewBox="0 0 14 14"><circle cx="7" cy="7" r="5" fill="none" stroke="var(--rust)" stroke-width="2"/></svg>speaking</li>
      <li><svg viewBox="0 0 14 14"><circle cx="7" cy="7" r="5" fill="none" stroke="var(--rust)" stroke-width="2"/></svg>articles</li>
    </ul>
    <h2 class="script-name back-name">Norah Pellow</h2>
    <p class="credentials">PhD, MCR, BAppSci, DipHum, AssDipEd<br>ABN 00 000 000 00</p>
    <p class="contact contact--phone">0400 555 218 (m)<br>+61 3 9000 4127 (h)</p>
    <p class="contact contact--web">norah@norahpellow.com<br><span class="site">norahpellow.com</span></p>
  </section>
</body>
</html>
```